Business Card Design for a Lending Business (Hard Money loans)

We need a business card for our Real Estate Lending business. We do hard Money loans for real estate investors. We have an existing logo we like, see attached. I'd like the business card to mostly include the logo colors, but a bright color pop of some sort would be nice to see also. Card should include Logo, Company Name, Company Address, Employee Name, Cell Phone, Main Phone, Email, Website

Industry/Entity Type

Finance / Lending

Contact Information for Business Card

Logo, Company Name, Company Address, Employee Name, Cell Phone, Main Phone, Email, Website

Requirements
Nice to have
• I'd like the business card to mostly include the logo colors, but a bright color pop of some sort would be nice to see also.

```html
<!DOCTYPE html>
<html lang="en">
<head>
<meta charset="utf-8">
<title>Keystone Lending – Business Card</title>
<link href="https://fonts.googleapis.com/css2?family=Arimo:wght@400;700&display=swap" rel="stylesheet">
<style>
  :root {
    --navy: #02288a;
    --navy-deep: #0a2a80;
    --sky: #12a6dc;
    --white: #ffffff;
    --ink: #2b2b2b;
    --muted: #7a7a7a;
    --backdrop: #3a3a3a;
    --rule: #d6d6d6;
  }
  * { box-sizing: border-box; margin: 0; padding: 0; }
  html, body {
    width: 1200px; height: 689px; overflow: hidden;
    background: var(--backdrop);
    font-family: "Arimo", Arial, sans-serif;
  }
  .stage {
    position: relative; width: 1200px; height: 689px;
    display: flex; align-items: center; justify-content: center; gap: 40px;
  }
  .card {
    width: 540px; height: 310px; border-radius: 18px;
    position: relative; overflow: hidden;
    box-shadow: 0 10px 30px rgba(0,0,0,.35);
  }
  /* Front */
  .card-front {
    background: var(--navy);
    display: flex; flex-direction: column; align-items: center; justify-content: center;
    color: var(--white);
  }
  .brand { display: flex; flex-direction: column; align-items: center; }
  .brand-dot {
    width: 62px; height: 62px; border-radius: 50%;
    background: var(--sky); margin-bottom: 18px;
  }
  .brand-name {
    font-weight: 700; font-size: 38px; letter-spacing: 4px; text-transform: uppercase;
    line-height: 1;
  }
  .brand-sub {
    font-weight: 700; font-size: 38px; letter-spacing: 4px; text-transform: uppercase;
    line-height: 1.1;
  }
  .brand-rule {
    width: 290px; height: 2px; background: var(--sky); margin-top: 12px;
  }
  .front-url { font-size: 14px; margin-top: 26px; letter-spacing: .3px; }

  /* Back */
  .card-back { background: var(--white); display: flex; }
  .back-brand {
    width: 58%; display: flex; flex-direction: column; align-items: center; justify-content: center;
    color: var(--navy-deep);
  }
  .back-brand .brand-name, .back-brand .brand-sub { font-size: 32px; letter-spacing: 3px; }
  .back-brand .brand-rule { width: 240px; }
  .divider {
    width: 1px; margin: 28px 0; background: linear-gradient(var(--white), var(--rule) 30%, var(--rule) 70%, var(--white));
  }
  .contact {
    flex: 1; padding: 46px 22px 0 22px; color: var(--ink);
  }
  .person-name { color: var(--navy-deep); font-weight: 700; font-size: 22px; }
  .person-title { color: var(--muted); font-size: 12px; margin-top: 2px; }
  .address { font-size: 13px; line-height: 1.4; margin-top: 20px; }
  .channels { list-style: none; margin-top: 14px; font-size: 13px; line-height: 1.5; }
  .channels li { display: flex; align-items: center; gap: 8px; }
  .channels svg { width: 12px; height: 12px; flex: none; fill: var(--sky); }
</style>
</head>
<body>
<main class="stage">
  <section class="card card-front" aria-label="Card front">
    <div class="brand">
      <span class="brand-dot"></span>
      <span class="brand-name">Keystone</span>
      <span class="brand-sub">Lending</span>
      <span class="brand-rule"></span>
    </div>
    <p class="front-url">www.keystonelending.com</p>
  </section>

  <section class="card card-back" aria-label="Card back">
    <div class="back-brand">
      <span class="brand-dot"></span>
      <span class="brand-name">Keystone</span>
      <span class="brand-sub">Lending</span>
      <span class="brand-rule"></span>
    </div>
    <div class="divider"></div>
    <div class="contact">
      <h1 class="person-name">Daniel Reyes</h1>
      <p class="person-title">President</p>
      <p class="address">4120 Juniper Court<br>Fairview, Canada 20931</p>
      <ul class="channels">
        <li><svg viewBox="0 0 12 12"><path d="M3 0l2 3-1.3 1.3a7 7 0 0 0 4 4L9 7l3 2-1.5 2.5C5 11 1 7 .5 1.5z"/></svg>555-210-4837</li>
        <li><svg viewBox="0 0 12 12"><path d="M3 0h6a1 1 0 0 1 1 1v10a1 1 0 0 1-1 1H3a1 1 0 0 1-1-1V1a1 1 0 0 1 1-1zm0 2v7h6V2z"/></svg>555-318-6925</li>
        <li><svg viewBox="0 0 12 12"><path d="M0 2h12v8H0zm1 1l5 4 5-4z"/></svg>info@keystonelending.com</li>
        <li><svg viewBox="0 0 12 12"><circle cx="6" cy="6" r="6"/></svg>www.keystonelending.com</li>
      </ul>
    </div>
  </section>
</main>
</body>
</html>
```